Corridor Works

Small ageny public transit advocacy, funding and compliance.
Consulting and lobbying efforts for small public transit agencies and communities exploring public transit opportunities.

I was interested in a simple line sketch suggesting motion, mobility. The card will be black on white. I would like it to include the bUs ones brief; Advocacy, Funding , and Compliance for small transit agencies.

Reason: I have been traveling and have had limited time to respond. Thank you all for your submit talks.

Industry/Entity Type

Consulting

Contact Information for Business Card

Paul R Vesby
Phone (907) 418-2960
Email paulrvesby@mailnook.net

```html
<!DOCTYPE html>
<html lang="en">
<head>
<meta charset="utf-8">
<title>Corridor Works – Business Card</title>
<link rel="stylesheet" href="https://fonts.googleapis.com/css2?family=Saira:wght@400;600&display=swap">
<style>
  :root {
    --backdrop: #d9d6d2;
    --card: #ffffff;
    --ink: #111111;
    --band-text: #ffffff;
    --shadow: rgba(0, 0, 0, 0.25);
  }
  * { margin: 0; padding: 0; box-sizing: border-box; }
  html, body {
    width: 1200px;
    height: 800px;
    overflow: hidden;
    background: var(--backdrop);
  }
  .canvas {
    position: relative;
    width: 1200px;
    height: 800px;
  }
  .business-card {
    position: absolute;
    left: 180px;
    top: 160px;
    width: 840px;
    height: 480px;
    background: var(--card);
    box-shadow: 0 10px 30px var(--shadow);
    font-family: "Saira", sans-serif;
    color: var(--ink);
  }
  .brand {
    position: absolute;
    left: 0;
    right: 0;
    top: 36px;
    display: flex;
    flex-direction: column;
    align-items: center;
  }
  .brand-mark {
    width: 130px;
    height: 130px;
    display: block;
  }
  .brand-name {
    margin-top: 10px;
    font-size: 44px;
    font-weight: 600;
    line-height: 1;
    letter-spacing: 0.5px;
  }
  .tagline-band {
    position: absolute;
    left: 0;
    right: 0;
    top: 250px;
    height: 30px;
    background: var(--ink);
    color: var(--band-text);
    display: flex;
    align-items: center;
    justify-content: center;
    font-size: 15px;
    font-variant: small-caps;
    letter-spacing: 3px;
  }
  .contact {
    position: absolute;
    left: 250px;
    right: 0;
    top: 300px;
    text-align: center;
  }
  .contact-name {
    font-size: 34px;
    font-weight: 600;
    letter-spacing: 1px;
  }
  .contact-phone {
    margin-top: 22px;
    font-size: 36px;
    font-weight: 400;
    letter-spacing: 2px;
    line-height: 1.1;
  }
  .contact-email {
    font-size: 26px;
    font-weight: 400;
    letter-spacing: 3px;
  }
</style>
</head>
<body>
<main class="canvas">
  <section class="business-card">
    <div class="brand">
      <svg class="brand-mark" viewBox="0 0 130 130" aria-hidden="true">
        <circle cx="65" cy="65" r="62" fill="var(--ink)"/>
      </svg>
      <div class="brand-name">Corridor Works</div>
    </div>
    <div class="tagline-band">Advocacy, Funding , and Compliance for small transit agencies</div>
    <div class="contact">
      <div class="contact-name">Paul R Vesby</div>
      <div class="contact-phone">(907) 418-2960</div>
      <div class="contact-email">paulrvesby@mailnook.net</div>
    </div>
  </section>
</main>
</body>
</html>
```